Window posters

We want a design (Smiley tooth shaped/logo attached) that will be posted on a dental office windows (23"x23") with 11 different wording/colors for each tooth.
All 11 will have the office name on top (Maple lane smiles) then:
1- Friendly dental place, Family dentistry.
2- Comprehensive, periodic, exams, cleanings, X-rays
3- Urgent care dentistry, dental emergencies, dental pain.
4- Extractions, immediate Guided implants, 3D scans.
5- Painless one day root canal treatment, conservative dentistry.
6- Cosmetic dentistry, bonding, digital smile makeover.
7- Clear aligners, Trua grin, Clarobrace.
8- Same day crowns and bridges.
9- Partial and complete dentures, implants Overdenture.
10- All teeth fixed on Implants.
11- Sleep apnea appliances, sleep dentistry.

```html
<!DOCTYPE html>
<html lang="en">
<head>
<meta charset="utf-8">
<title>Maple Lane Smiles – Window Poster 2</title>
<link rel="stylesheet" href="https://fonts.googleapis.com/css2?family=Barlow+Semi+Condensed:wght@600;700&display=swap">
<style>
  :root {
    --sky-light: #ffffff;
    --sky-mid: #dff3fb;
    --sky-deep: #8fd6f0;
    --brand-blue: #1658a3;
    --band-blue: #104d8f;
    --accent-teal: #16d3c9;
    --accent-teal-edge: #0fa89f;
    --text-white: #ffffff;
    --text-highlight: #90d5f6;
  }
  * { margin: 0; padding: 0; box-sizing: border-box; }
  html, body {
    width: 1200px;
    height: 1199px;
    overflow: hidden;
    background: var(--sky-light);
  }
  .poster {
    position: relative;
    width: 1200px;
    height: 1199px;
    overflow: hidden;
    font-family: "Barlow Semi Condensed", "Arial Narrow", sans-serif;
  }
  .poster__backdrop {
    position: absolute;
    inset: 0;
    background:
      radial-gradient(ellipse 70% 55% at 50% 42%, var(--sky-light) 0%, rgba(255,255,255,0.85) 45%, rgba(255,255,255,0) 80%),
      linear-gradient(160deg, var(--sky-deep) 0%, var(--sky-mid) 40%, var(--sky-light) 70%, var(--sky-mid) 100%);
  }
  .office-name {
    position: absolute;
    top: 40px;
    left: 0;
    width: 100%;
    text-align: center;
    color: var(--brand-blue);
    font-weight: 700;
    text-transform: uppercase;
    line-height: 1;
  }
  .office-name__line--top {
    display: block;
    font-size: 78px;
    letter-spacing: 4px;
  }
  .office-name__line--main {
    display: block;
    font-size: 150px;
    letter-spacing: 2px;
    margin-top: 2px;
  }
  .brand-mark {
    position: absolute;
    left: 390px;
    top: 350px;
    width: 420px;
    height: 420px;
  }
  .service-band {
    position: absolute;
    left: 0;
    top: 820px;
    width: 1200px;
    height: 379px;
  }
  .service-list {
    position: absolute;
    right: 92px;
    top: 955px;
    text-align: right;
    font-weight: 600;
    font-size: 82px;
    line-height: 98px;
    color: var(--text-white);
    letter-spacing: 0.5px;
  }
  .service-list__item--highlight { color: var(--text-highlight); }
</style>
</head>
<body>
  <main class="poster">
    <div class="poster__backdrop" role="img" aria-label="Soft light-blue faceted geometric background"></div>

    <h1 class="office-name">
      <span class="office-name__line--top">Maple Lane</span>
      <span class="office-name__line--main">Smiles</span>
    </h1>

    <svg class="brand-mark" viewBox="0 0 420 420" aria-hidden="true">
      <circle cx="210" cy="210" r="200" fill="var(--accent-teal)" stroke="var(--accent-teal-edge)" stroke-width="6"/>
    </svg>

    <svg class="service-band" viewBox="0 0 1200 379" preserveAspectRatio="none" aria-hidden="true">
      <defs>
        <linearGradient id="accentStripe" x1="0" y1="0" x2="1" y2="0">
          <stop offset="0" stop-color="var(--band-blue)"/>
          <stop offset="0.55" stop-color="#1f7fb0"/>
          <stop offset="1" stop-color="var(--accent-teal)"/>
        </linearGradient>
      </defs>
      <polygon points="0,17 1200,60 1200,379 0,379" fill="var(--band-blue)"/>
      <polygon points="0,17 1200,60 1200,100 0,21" fill="url(#accentStripe)"/>
      <polygon points="0,21 1200,100 1200,112 0,24" fill="var(--text-white)"/>
    </svg>

    <p class="service-list">
      Comprehensive, <span class="service-list__item--highlight">PERIODIC</span><br>
      <span class="service-list__item--highlight">EXAMS,</span> Cleanings, <span class="service-list__item--highlight">X-rays</span>
    </p>
  </main>
</body>
</html>
```